STICKER DESIGN required for packaging. UK START UP TEA BUSINESS

We are looking for a design for a sticker that will be applied to packaging for our teas! We are a new start up Tea business based in the UK called 'BrookLeafs'
Selling quality loose leaf tea and teabags via our online shop and also face to face at farmers markets / food shows and eventually in our own tea emporium. We will be marketing our teas to hotels, cafes, delis etc. too
We carry every day teas eg. breakfast blends and also speciality and rare teas to offer customers the chance to try something new. Tea as a treat / ritual / indulgence / healthy lifestyle choice / modern
The design will initially be printed on vinyl stickers and then applied to the tea packaging (pouch bags in matte black and matte silver), in the future the design may be printed direct onto our packaging. The sticker design will need to be scalable as the size of the pouch bag varies dependant on the tea.
The sticker we have in mind is a leaf shape (sketch attached)
colour green to match our logo
It will include our logo (files attached)
Text to be included on the sticker is
- www.brookleafs.co.uk
- Welbury, England
- The tea type eg. Green
It will need to complement both black and silver pouches that we are using to package our teas (see attached image of our pouches)
Colours - green leaf, see our corporate colours (green & orange) on our logo files attached. We also like silver and black.
Font - nothing to swirly, must be easy to read on the packaging
once a sticker design is agreed for the initial tea type (Green) we will require additional files for each tea type that we stock. Just the tea type (Green) to be updated - the rest of the design to stay the same. The tea types we stock are listed below
Green
Black
Oolong
White
Herbal
Blended
Happy to answer any questions and aim to give feedback daily! Thank you for your interest

```html
<!DOCTYPE html>
<html lang="en">
<head>
<meta charset="utf-8">
<title>BrookLeafs – Green Tea Sticker</title>
<link rel="stylesheet" href="https://fonts.googleapis.com/css2?family=Raleway:wght@400;500&display=swap">
<style>
  :root {
    --page: #ffffff;
    --silver-pouch: #9b9b9b;
    --black-pouch: #0a0b0a;
    --sticker-shadow: #4a545a;
    --sticker-rim: #ffffff;
    --leaf-green: #42d400;
    --leaf-green-light: #52e014;
    --brand-orange: #f26b1d;
    --type-green: #6cd80a;
    --label-white: #ffffff;
  }
  html, body {
    margin: 0;
    padding: 0;
    width: 1200px;
    height: 700px;
    overflow: hidden;
    background: var(--page);
  }
  .presentation {
    display: block;
    width: 1200px;
    height: 700px;
  }
  .pouch--silver { fill: var(--silver-pouch); }
  .pouch--black { fill: var(--black-pouch); }
  .sticker__shadow { fill: var(--sticker-shadow); }
  .sticker__rim { fill: var(--sticker-rim); }
  .sticker__leaf { fill: var(--leaf-green); }
  .sticker__leaf-highlight { fill: var(--leaf-green-light); }
  .sticker__web,
  .sticker__place {
    font-family: "Raleway", sans-serif;
    font-weight: 400;
    fill: var(--brand-orange);
  }
  .sticker__web { font-size: 13px; letter-spacing: 0.3px; }
  .sticker__place { font-size: 11px; letter-spacing: 0.4px; text-transform: uppercase; }
  .sticker__brand {
    font-family: "Raleway", sans-serif;
    font-weight: 500;
    font-size: 36px;
    fill: var(--brand-orange);
  }
  .sticker__type-badge { fill: var(--label-white); }
  .sticker__type {
    font-family: "Raleway", sans-serif;
    font-weight: 500;
    font-size: 28px;
    fill: var(--type-green);
  }
</style>
</head>
<body>
<svg class="presentation" viewBox="0 0 1200 700" xmlns="http://www.w3.org/2000/svg" xmlns:xlink="http://www.w3.org/1999/xlink">
  <defs>
    <path id="leaf-inner" d="M246,116 H386 A6,6 0 0 1 392,122 V262 A146,146 0 1 1 246,116 Z"/>
    <clipPath id="leaf-clip">
      <use href="#leaf-inner"/>
    </clipPath>
    <path id="web-arc" d="M132,328 A126,126 0 0 1 183,153"/>
    <path id="place-arc" d="M209,393 A136,136 0 0 0 369,319"/>

    <symbol id="tea-sticker" viewBox="0 0 500 500" width="500" height="500">
      <g transform="translate(14,-26)">
        <path class="sticker__shadow" d="M246,84 H394 A30,30 0 0 1 424,114 V262 A178,178 0 1 1 246,84 Z"/>
      </g>
      <path class="sticker__rim" d="M246,84 H394 A30,30 0 0 1 424,114 V262 A178,178 0 1 1 246,84 Z"/>
      <use class="sticker__leaf" href="#leaf-inner"/>
      <polygon class="sticker__leaf-highlight" clip-path="url(#leaf-clip)" points="90,100 300,100 270,260 300,420 90,420"/>

      <text class="sticker__web"><textPath href="#web-arc" startOffset="4">www.brookleafs.co.uk</textPath></text>
      <text class="sticker__brand" x="290" y="240" text-anchor="middle">BrookLeafs</text>

      <ellipse class="sticker__type-badge" cx="250" cy="318" rx="57" ry="30"/>
      <text class="sticker__type" x="250" y="328" text-anchor="middle">Green</text>

      <text class="sticker__place"><textPath href="#place-arc" startOffset="14">Welbury, England</textPath></text>
    </symbol>
  </defs>

  <g class="mockup mockup--silver">
    <rect class="pouch--silver" x="64" y="100" width="500" height="500"/>
    <use href="#tea-sticker" x="64" y="100" width="500" height="500"/>
  </g>

  <g class="mockup mockup--black">
    <rect class="pouch--black" x="640" y="100" width="500" height="500"/>
    <use href="#tea-sticker" x="640" y="100" width="500" height="500"/>
  </g>
</svg>
</body>
</html>
```